India Export Business Card Design

We are a small company importing from India,
Antique furniture and textiles.
We would like a design with somthing of India in it.
IE: Camels, Tuk Tuks, People or maybe Taj Mahal.
Only one of the above suggestions, we do not want the card to be to busy.
We travel to India twice a year to get the product and then come home to New Zealand and sell it.
And must have our business name which is
Velmora Trading Company
Nz phone no. 64 9 317 6825
Mobile 64 21 573 162
Email bethany@velmoratrading.co.nz
Www.velmoratrading.co.nz

Also my name and position
Bethany Crowhurst
Director

Reason: I am awaiting for a design to come back with different colours. Many thanks

Target Market(s)

Indian heritage furniture and textiles in India also
New Zealand market for public to buy the goods that is bought in India

Industry/Entity Type

Travel

Contact Information for Business Card

Velmora Trading Company
17b Harlow Lane
RD 7 Papakura 2590
Auckland
New Zealand
email address which will be associated to our new website
website once we have it assigned

Requirements
Must have
• Company name and region.
Phone numbers
My name and title.
Nice to have
• I would like the card to portray India and as i said before, I like the idea of camels in a line with ropes between them like an animation.
But happy to see what other suggestions there are.

```html
<!DOCTYPE html>
<html lang="en">
<head>
<meta charset="utf-8">
<title>Velmora Trading Company – Business Card</title>
<link href="https://fonts.googleapis.com/css2?family=Arimo:wght@400;700&display=swap" rel="stylesheet">
<style>
  :root {
    --canvas: #e6ebe9;
    --card-back: #ffffff;
    --brand-magenta: #c2338a;
    --text-dark: #2e2e2e;
    --label-red: #f2303a;
    --front-orange: #e8531e;
    --front-peach: #f4a36a;
    --front-pink: #d9467f;
    --front-rose: #c93170;
    --ornament-white: #ffffff;
  }
  * { margin: 0; padding: 0; box-sizing: border-box; }
  html, body { width: 1200px; height: 900px; overflow: hidden; }
  body {
    background: var(--canvas);
    font-family: "Arimo", Helvetica, Arial, sans-serif;
    position: relative;
  }
  .card { position: absolute; left: 293px; width: 572px; height: 350px; }
  .card-front { top: 64px; overflow: hidden; }
  .card-front .texture {
    position: absolute; inset: 0;
    background:
      radial-gradient(ellipse at 20% 30%, rgba(246,180,110,.75), transparent 55%),
      radial-gradient(ellipse at 85% 85%, rgba(246,170,130,.7), transparent 45%),
      linear-gradient(100deg, var(--front-orange) 0%, var(--front-peach) 30%, var(--front-pink) 60%, var(--front-rose) 85%, var(--front-peach) 100%);
  }
  .dashed-frame { position: absolute; inset: 0; }
  .cartouche {
    position: absolute; left: 140px; top: 40px; width: 292px; height: 268px;
    background: var(--ornament-white);
    border-radius: 46% 46% 46% 46% / 40% 40% 40% 40%;
  }
  .mandala {
    position: absolute; top: 138px; width: 76px; height: 76px; border-radius: 50%;
    background: radial-gradient(circle, rgba(255,235,240,.85) 0%, rgba(255,220,225,.55) 60%, rgba(255,220,225,0) 72%);
  }
  .mandala.left { left: 48px; }
  .mandala.right { left: 450px; }
  .brand {
    position: absolute; left: 0; right: 0; text-align: center;
    color: var(--brand-magenta); font-weight: 700; text-transform: uppercase; line-height: 1;
  }
  .brand .line-1 { display: block; font-size: 24px; letter-spacing: 1px; }
  .brand .line-2 { display: block; font-size: 18px; letter-spacing: 1px; margin-top: 6px; }
  .card-front .brand { top: 166px; }
  .card-back { top: 462px; background: var(--card-back); }
  .card-back .brand { top: 28px; }
  .holder {
    position: absolute; top: 136px; left: 0; right: 0; text-align: center;
    color: var(--text-dark); font-size: 20px; line-height: 25px;
  }
  .holder .title { font-weight: 700; }
  .address {
    position: absolute; top: 229px; left: 0; right: 0; text-align: center;
    color: var(--text-dark); font-size: 16px; font-weight: 700; line-height: 20px;
  }
  .contacts {
    position: absolute; top: 280px; left: 0; right: 0; text-align: center;
    color: var(--text-dark); font-size: 16px; line-height: 24px; white-space: nowrap;
  }
  .contacts .label { color: var(--label-red); font-weight: 700; }
</style>
</head>
<body>
  <section class="card card-front">
    <div class="texture" role="img" aria-label="Warm orange and pink painted texture background"></div>
    <svg class="dashed-frame" width="572" height="350" viewBox="0 0 572 350">
      <rect x="20" y="20" width="533" height="309" fill="none" stroke="#ffffff" stroke-width="2" stroke-dasharray="9 6"/>
    </svg>
    <div class="mandala left" role="img" aria-label="Round mandala ornament"></div>
    <div class="mandala right" role="img" aria-label="Round mandala ornament"></div>
    <div class="cartouche" role="img" aria-label="White ornamental cartouche with leaf petals"></div>
    <div class="brand">
      <span class="line-1">Velmora Trading</span>
      <span class="line-2">Company</span>
    </div>
  </section>

  <section class="card card-back">
    <div class="brand">
      <span class="line-1">Velmora Trading</span>
      <span class="line-2">Company</span>
    </div>
    <div class="holder">
      <div class="name">Bethany Crowhurst</div>
      <div class="title">Director</div>
    </div>
    <div class="address">
      <div>Velmora Trading Company - 17b Harlow Lane</div>
      <div>7 Papakura 2590 - Auckland New Zealand</div>
    </div>
    <div class="contacts">
      <div><span class="label">Phone:</span> 64 9 317 6825 (nz) <span class="label">Mobile:</span> 64 21 573 162</div>
      <div><span class="label">Email:</span> bethany@velmoratrading.co.nz <span class="label">Web:</span> www.velmoratrading.co.nz</div>
    </div>
  </section>
</body>
</html>
```